Designs of screens for job search mobile app

Design the following screens:

1. Login
2. Job search results in tabs
3. Job details in cards format
4. Profile
5. Settings

Logo and references are provided. The app need to be playful, easy to use, different from traditional job search app like Hirevo, Workbrix and others and targeted to Millennial users (age 18-30).

The main app reference is Pogura, in terms of the colorful and fun color and font scheme.

Target Market(s)

Millennial users (age 18-30).

Requirements
Must have
• A fun, playful feel

```html
<!DOCTYPE html>
<html lang="en">
<head>
<meta charset="utf-8">
<title>Jobtrail – App Screens</title>
<link href="https://fonts.googleapis.com/css2?family=Roboto:wght@300;400;500&display=swap" rel="stylesheet">
<style>
:root{
  --teal:#00b7b1;
  --teal-deep:#0b9086;
  --action-blue:#2b94d2;
  --ink:#333a3f;
  --muted:#9aa3a8;
  --line:#d8e4e6;
  --divider:#8fd9d6;
  --panel:#e9edef;
  --row:#f8f9f9;
  --white:#ffffff;
  --alert:#f03c3c;
  --toggle-on:#4cd964;
}
*{box-sizing:border-box;margin:0;padding:0}
html,body{width:1200px;height:1200px;overflow:hidden}
body{font-family:"Roboto",sans-serif;color:var(--ink);
  background:linear-gradient(135deg,#8b8ed9 0%,#93b7e2 45%,#7aa6d8 70%,#5d8fcd 100%)}
.stage{position:absolute;left:0;top:0;width:1500px;height:1500px;transform:scale(.8);transform-origin:0 0}
.screen{position:absolute;width:274px;overflow:hidden;background:var(--panel);box-shadow:0 4px 14px rgba(40,60,110,.18)}
.status{height:18px;display:flex;justify-content:space-between;align-items:center;padding:0 6px;font-size:10px;color:var(--white)}
.status .bat{display:inline-block;width:20px;height:8px;background:var(--white);border-radius:1px;vertical-align:middle;margin-left:3px}
.header{background:var(--teal)}
.titlebar{height:36px;display:flex;align-items:center;justify-content:center;position:relative;color:var(--white);font-size:12px}
.titlebar .left,.titlebar .right{position:absolute;top:9px;width:18px;height:18px;color:var(--white)}
.titlebar .left{left:10px}.titlebar .right{right:10px}
svg.icon{fill:none;stroke:currentColor;stroke-width:1.3;stroke-linecap:round;stroke-linejoin:round}
.tabbar{position:absolute;left:0;right:0;bottom:0;height:42px;background:#f5f6f6;border-top:1px solid var(--line);display:flex}
.tab{flex:1;display:flex;flex-direction:column;align-items:center;justify-content:center;font-size:8px;color:var(--muted);gap:2px}
.tab svg{width:19px;height:19px}
.tab.active{color:var(--teal);background:#eaf4f4}
.photo{position:absolute;inset:0}
.btn{display:flex;align-items:center;justify-content:center;color:var(--white);font-size:12px;background:var(--teal)}
.splash{background:var(--teal-deep)}
.brand{position:absolute;top:202px;left:0;right:0;display:flex;justify-content:center;align-items:center;gap:8px;color:var(--white);font-size:26px;font-weight:400}
.brand .dot{width:30px;height:30px;border-radius:50%;border:2px solid #6fd3cc}
.spinner{position:absolute;left:130px;top:278px;width:14px;height:14px;border-radius:50%;border:2px dotted rgba(255,255,255,.6)}
.field{position:absolute;left:47px;width:180px;height:20px;border-bottom:1px solid rgba(255,255,255,.55);display:flex;align-items:center;gap:8px;font-size:10px;color:rgba(255,255,255,.45)}
.field svg{width:11px;height:11px;color:rgba(255,255,255,.8)}
.result-count{text-align:center;font-size:10px;padding:9px 0 6px;color:var(--ink)}
.card{background:var(--white);border-radius:6px;margin:0 6px 6px;height:79px;position:relative}
.logo-box{position:absolute;left:8px;top:7px;width:92px;height:50px;display:flex;align-items:center;justify-content:center;gap:5px;font-size:13px;font-weight:500;color:#2a4f9e}
.logo-box .mark{width:12px;height:12px;border-radius:50%;background:#2a4f9e}
.logo-box.nex{color:#1577c9}.logo-box.nex .mark{background:#1577c9}
.co-name{position:absolute;left:0;width:108px;bottom:6px;text-align:center;font-size:10px;color:#707a80}
.job{position:absolute;left:114px;top:8px;font-size:11px;line-height:1.1}
.job small{display:block;font-size:9px;color:var(--muted);line-height:1.25}
.job small:first-of-type{margin-top:2px}
.ago{position:absolute;right:9px;bottom:6px;font-size:8.5px;color:var(--muted)}
.row{height:44px;background:var(--row);border-bottom:1px solid var(--line);display:flex;align-items:center;padding:0 9px;font-size:11.5px}
.row .grow{flex:1}
.row svg.plus{width:19px;height:19px;color:var(--teal)}
.form-row{height:44px;background:var(--row);border-bottom:1px solid var(--line);display:flex;align-items:center;padding:0 9px;font-size:11.5px}
.form-row .lbl{color:var(--muted);flex:1}
.form-row .lbl i{font-style:normal;font-size:8px}
.toggle{width:44px;height:26px;border-radius:13px;position:relative;background:var(--white);border:1px solid #d0d6d8}
.toggle::after{content:"";position:absolute;top:1px;left:1px;width:22px;height:22px;border-radius:50%;background:var(--white);box-shadow:0 1px 3px rgba(0,0,0,.3)}
.toggle.on{background:var(--toggle-on);border-color:var(--toggle-on)}
.toggle.on::after{left:19px}
.chip{position:absolute;height:26px;border:1px solid var(--divider);border-radius:13px;background:var(--white);display:flex;align-items:center;padding-left:11px;font-size:11px}
.chip .minus{position:absolute;right:3px;top:3px;width:18px;height:18px;border-radius:50%;background:var(--alert)}
.chip .minus::after{content:"";position:absolute;left:5px;right:5px;top:8px;height:2px;background:var(--white)}
.avatar{width:40px;height:40px;border-radius:50%;border:2px solid var(--teal)}
.pager{display:flex;gap:5px;justify-content:center}
.pager span{width:6px;height:6px;border-radius:50%;background:#a6dedc}
.pager span.on{background:var(--teal)}
</style>
</head>
<body>
<svg width="0" height="0" style="position:absolute">
  <defs>
    <symbol id="i-home" viewBox="0 0 20 20"><path d="M3 10 10 3l7 7M5 8.5V17h4v-4h2v4h4V8.5"/></symbol>
    <symbol id="i-search" viewBox="0 0 20 20"><circle cx="8.5" cy="8.5" r="5.5"/><path d="m12.5 12.5 5 5"/></symbol>
    <symbol id="i-jobs" viewBox="0 0 20 20"><circle cx="10" cy="10" r="7.5"/><circle cx="10" cy="8" r="2.8"/><path d="M5.5 15.5c1-2.5 8-2.5 9 0"/></symbol>
    <symbol id="i-cv" viewBox="0 0 20 20"><rect x="4.5" y="2.5" width="11" height="15" rx="1"/><path d="M7 6h6M7 9h6M7 12h6M7 15h4"/></symbol>
    <symbol id="i-gear" viewBox="0 0 20 20"><circle cx="10" cy="10" r="2.6"/><circle cx="10" cy="10" r="6"/><path d="M10 2v2M10 16v2M2 10h2M16 10h2M4.3 4.3l1.4 1.4M14.3 14.3l1.4 1.4M4.3 15.7l1.4-1.4M14.3 5.7l1.4-1.4"/></symbol>
    <symbol id="i-plus" viewBox="0 0 20 20"><circle cx="10" cy="10" r="8.5"/><path d="M10 5.5v9M5.5 10h9"/></symbol>
    <symbol id="i-edit" viewBox="0 0 20 20"><path d="M15 11v6H3V5h6"/><path d="m9 12 1-3 7-7 2 2-7 7z"/></symbol>
    <symbol id="i-share" viewBox="0 0 20 20"><path d="M6 8H3v10h14V8h-3M10 13V2M6.5 5.5 10 2l3.5 3.5"/></symbol>
    <symbol id="i-back" viewBox="0 0 20 20"><path d="M13 3 6 10l7 7"/></symbol>
    <symbol id="i-close" viewBox="0 0 20 20"><path d="m4 4 12 12M16 4 4 16"/></symbol>
    <symbol id="i-pin" viewBox="0 0 20 20"><path d="M10 18s-5-6-5-10a5 5 0 0 1 10 0c0 4-5 10-5 10z"/><circle cx="10" cy="8" r="1.6"/></symbol>
    <symbol id="i-globe" viewBox="0 0 20 20"><circle cx="10" cy="10" r="7.5"/><path d="M2.5 10h15M10 2.5c3 3 3 12 0 15M10 2.5c-3 3-3 12 0 15"/></symbol>
    <symbol id="i-chev" viewBox="0 0 20 20"><path d="m4 7 6 6 6-6"/></symbol>
  </defs>
</svg>

<div class="stage">

  <!-- Splash -->
  <section class="screen splash" style="left:76px;top:49px;height:485px">
    <div class="brand"><span class="dot"></span>Jobtrail</div>
    <div class="spinner"></div>
  </section>

  <!-- Login -->
  <section class="screen" style="left:431px;top:49px;height:485px;background:#555b60">
    <div class="photo" role="img" aria-label="Blurred background photo of a person at work" style="background:radial-gradient(ellipse at 50% 35%,#7d7b7a 0%,#4f5559 55%,#3c4247 100%)"></div>
    <div class="status" style="position:relative"><span>●●●●● Telvo</span><span>9:41 AM</span><span>100%<span class="bat"></span></span></div>
    <div style="position:absolute;top:214px;left:0;right:0;text-align:center;color:#fff;font-size:12px">PRODUCT DEMO SLIDES</div>
    <div class="pager" style="position:absolute;top:354px;left:0;right:0"><span style="background:#fff"></span><span style="background:rgba(255,255,255,.5)"></span><span style="background:rgba(255,255,255,.5)"></span></div>
    <div class="btn" style="position:absolute;top:384px;left:47px;width:180px;height:31px;background:var(--action-blue)">Login with Chatterly</div>
    <div style="position:absolute;top:435px;left:0;right:0;text-align:center;color:rgba(255,255,255,.75);font-size:10px">Join now</div>
  </section>

  <!-- Search -->
  <section class="screen" style="left:793px;top:49px;height:485px">
    <div class="photo" role="img" aria-label="Blurred background photo of an office scene" style="background:radial-gradient(ellipse at 40% 45%,#8a8380 0%,#5a5552 50%,#2f2d2c 100%)"></div>
    <div class="status" style="position:relative"><span>●●●●● Telvo</span><span>9:41 AM</span><span>100%<span class="bat"></span></span></div>
    <div class="field" style="top:143px"><svg class="icon"><use href="#i-search"/></svg>Job title, keywords, company</div>
    <div class="field" style="top:174px"><svg class="icon"><use href="#i-globe"/></svg>Country</div>
    <div class="field" style="top:205px"><svg class="icon"><use href="#i-pin"/></svg>Location</div>
    <div class="btn" style="position:absolute;top:246px;left:47px;width:180px;height:31px">Search Jobs</div>
    <nav class="tabbar">
      <div class="tab"><svg class="icon"><use href="#i-home"/></svg>Home</div>
      <div class="tab active"><svg class="icon"><use href="#i-search"/></svg>Search</div>
      <div class="tab"><svg class="icon"><use href="#i-jobs"/></svg>My Jobs</div>
      <div class="tab"><svg class="icon"><use href="#i-cv"/></svg>My CV</div>
      <div class="tab"><svg class="icon"><use href="#i-gear"/></svg>Settings</div>
    </nav>
  </section>

  <!-- Results -->
  <section class="screen" style="left:1149px;top:49px;height:485px">
    <header class="header" style="height:54px">
      <div class="status"><span>●●●●● Telvo</span><span>9:41 AM</span><span>100%<span class="bat"></span></span></div>
      <div style="position:relative;height:36px">
        <svg class="icon" style="position:absolute;left:10px;top:8px;width:16px;height:18px;color:#fff"><use href="#i-back"/></svg>
        <div style="position:absolute;left:62px;top:5px;width:170px;height:24px;border-radius:3px;background:#19a3a0;color:#7fd3d0;font-size:10px;display:flex;align-items:center;gap:6px;padding-left:8px"><svg class="icon" style="width:10px;height:10px"><use href="#i-search"/></svg>Search</div>
      </div>
    </header>
    <div class="result-count">2048 Results</div>
    <article class="card">
      <div class="logo-box nex"><span class="mark"></span>Nexcore</div>
      <div class="co-name">NEXCORE INC</div>
      <div class="job">SOFTWARE ENGINEERS<small>Singapore</small><small>$80K - $90K per annum</small></div>
      <div class="ago">1 day ago</div>
    </article>
    <article class="card">
      <div class="logo-box"><span class="mark"></span>Axlen</div>
      <div class="co-name">AXLEN MOTORS</div>
      <div class="job">SYSTEM ARCHITECT<small>Singapore</small><small>$100K - $120K per annum</small><small>3 friends work / worked here</small></div>
      <div class="ago">2 hrs ago</div>
    </article>
    <article class="card">
      <div class="logo-box"><span class="mark"></span>Axlen</div>
      <div class="co-name">AXLEN MOTORS</div>
      <div class="job">SYSTEM ARCHITECT<small>Singapore</small><small>$100K - $120K per annum</small><small>3 friends work / worked here</small></div>
      <div class="ago">2 hrs ago</div>
    </article>
    <article class="card">
      <div class="logo-box"><span class="mark"></span>Axlen</div>
      <div class="co-name">AXLEN MOTORS</div>
      <div class="job">SYSTEM ARCHITECT<small>Singapore</small><small>$100K - $120K per annum</small><small>3 friends work / worked here</small></div>
      <div class="ago">2 hrs ago</div>
    </article>
    <article class="card">
      <div class="job">SYSTEM ARCHITECT</div>
    </article>
    <nav class="tabbar">
      <div class="tab"><svg class="icon"><use href="#i-home"/></svg>Home</div>
      <div class="tab active"><svg class="icon"><use href="#i-search"/></svg>Search</div>
      <div class="tab"><svg class="icon"><use href="#i-jobs"/></svg>My Jobs</div>
      <div class="tab"><svg class="icon"><use href="#i-cv"/></svg>My CV</div>
      <div class="tab"><svg class="icon"><use href="#i-gear"/></svg>Settings</div>
    </nav>
  </section>

  <!-- Job details -->
  <section class="screen" style="left:76px;top:562px;height:485px">
    <header class="header">
      <div class="status"><span>●●●●● Telvo</span><span>9:41 AM</span><span>100%<span class="bat"></span></span></div>
      <div class="titlebar"><svg class="icon left"><use href="#i-close"/></svg>Jobs Details<svg class="icon right"><use href="#i-share"/></svg></div>
    </header>
    <article style="position:absolute;top:85px;left:6px;width:262px;height:323px;background:#fff;border-radius:6px">
      <div class="logo-box" style="left:6px;top:4px"><span class="mark"></span>Axlen</div>
      <div class="co-name" style="top:59px;bottom:auto;width:106px">AXLEN MOTORS</div>
      <div class="job" style="left:114px;top:9px">SYSTEM ARCHITECT<small>Singapore</small><small>$100K - $120K per annum</small><small>3 friends work / worked here</small></div>
      <div class="ago" style="top:61px;bottom:auto">2 hrs ago</div>
      <div style="position:absolute;top:73px;left:0;right:0;border-top:1px solid var(--divider)"></div>
      <div style="position:absolute;top:82px;left:8px;font-size:11px">FRIENDS WORKING / WORKED HERE:</div>
      <div style="position:absolute;top:98px;left:8px;display:flex;gap:9px;font-size:9px;text-align:center">
        <div><div class="avatar" role="img" aria-label="Profile photo of Lucy" style="background:#c89b80"></div>Lucy</div>
        <div><div class="avatar" role="img" aria-label="Profile photo of Boris" style="background:#9d7e66"></div>Boris</div>
        <div><div class="avatar" role="img" aria-label="Profile photo of Bryant" style="background:#7e7470"></div>Bryant</div>
      </div>
      <div style="position:absolute;top:160px;left:0;right:0;border-top:1px solid var(--divider)"></div>
      <div style="position:absolute;top:167px;left:8px;right:8px;font-size:10px;line-height:1.28">
        <div style="font-size:11px">JOB DESCRIPTION:</div>
        Axlen Motor Company (Axlen), incorporated on July 9, 1919, is a global automotive and mobility company. The Company's principal business includes designing, manufacturing, marketing, financing and servicing a line of Axlen cars, trucks, sports utility vehicles (SUVs), and electrified vehicles, as well as Verlane luxury vehicles.
        <div style="margin-top:4px">SKILLS:</div>
        Python, PHP, C#
      </div>
    </article>
    <div class="pager" style="position:absolute;top:422px;left:0;right:0"><span class="on"></span><span></span><span></span></div>
    <div style="position:absolute;top:443px;left:6px;right:6px;display:flex;gap:6px">
      <div class="btn" style="flex:1;height:32px">Skip</div>
      <div class="btn" style="flex:1;height:32px;background:var(--action-blue)">Save</div>
      <div class="btn" style="flex:1;height:32px">Apply</div>
    </div>
  </section>

  <!-- Skills -->
  <section class="screen" style="left:76px;top:1080px;height:340px">
    <header class="header">
      <div class="status"><span>●●●●● Telvo</span><span>9:41 AM</span><span>100%<span class="bat"></span></span></div>
      <div class="titlebar"><svg class="icon left"><use href="#i-back"/></svg>Skills</div>
    </header>
    <div style="position:absolute;top:84px;left:0;right:0;height:160px;background:var(--row);border-top:1px solid var(--line);border-bottom:1px solid var(--line)">
      <div style="position:absolute;top:23px;left:10px;width:3px;height:3px;border-radius:50%;background:var(--ink)"></div>
      <div style="position:absolute;top:12px;left:20px;width:143px;height:20px;border:1px solid var(--divider);font-size:10.5px;padding:3px 5px">Marketing</div>
      <div class="btn" style="position:absolute;top:10px;left:176px;width:87px;height:24px">Add</div>
      <div style="position:absolute;top:44px;left:0;right:0;border-top:1px solid var(--line)"></div>
      <div class="chip" style="top:57px;left:9px;width:102px">Python<span class="minus"></span></div>
      <div class="chip" style="top:57px;left:115px;width:149px">Business Development<span class="minus"></span></div>
      <div class="chip" style="top:90px;left:9px;width:120px">C#<span class="minus"></span></div>
    </div>
    <div class="btn" style="position:absolute;top:275px;left:47px;width:180px;height:31px">Save</div>
  </section>

  <!-- My CV -->
  <section class="screen" style="left:431px;top:562px;height:805px">
    <header class="header">
      <div class="status"><span>●●●●● Telvo</span><span>9:41 AM</span><span>100%<span class="bat"></span></span></div>
      <div class="titlebar">My CV<svg class="icon right"><use href="#i-share"/></svg></div>
    </header>
    <div style="position:relative;height:214px;color:#fff;text-align:center">
      <div class="photo" role="img" aria-label="Dark blurred cover photo behind the profile" style="background:linear-gradient(180deg,#5e5552 0%,#3e3a3a 60%,#2f3134 100%)"></div>
      <div role="img" aria-label="Profile photo of Dane Holloway" style="position:absolute;left:104px;top:18px;width:66px;height:66px;border-radius:50%;border:2px solid var(--teal);background:#b08872"></div>
      <div style="position:absolute;top:92px;left:0;right:0;font-size:11.5px">Dane Holloway</div>
      <div style="position:absolute;top:108px;left:0;right:0;font-size:9px;line-height:1.3;color:#c7cbcd">Singapore<br>dane@mailbox.com</div>
      <div style="position:absolute;top:138px;left:0;right:0;font-size:11.5px;display:flex;justify-content:center;gap:10px">Add a headline to my profile<svg class="icon" style="width:18px;height:18px;color:#fff;margin-top:-5px"><use href="#i-edit"/></svg></div>
      <div style="position:absolute;top:162px;left:14px;right:14px;font-size:10px;line-height:1.25">Lorem ipsum dolor sit amet, consectetur Qui dicta minus molestive vel beatae natus eveniet ratione temporibus aperiam.</div>
    </div>
    <div style="background:var(--row);height:106px;position:relative;border-bottom:1px solid var(--divider)">
      <div style="position:absolute;left:9px;top:14px;font-size:11.5px">Work Experience</div>
      <svg class="icon" style="position:absolute;right:12px;top:12px;width:19px;height:19px;color:var(--teal)"><use href="#i-plus"/></svg>
      <div class="logo-box nex" style="left:8px;top:34px;width:88px;height:46px"><span class="mark"></span>Nexcore</div>
      <div style="position:absolute;left:0;width:104px;top:88px;text-align:center;font-size:10px;color:#707a80">NEXCORE INC</div>
      <div class="job" style="left:103px;top:38px">SOFTWARE ENGINEERS<small>Singapore</small><small>January 2015 to Present</small><small>(about 2 year)</small></div>
      <svg class="icon" style="position:absolute;right:12px;top:70px;width:18px;height:18px;color:var(--teal)"><use href="#i-edit"/></svg>
    </div>
    <div class="row"><span class="grow">Work Experience</span><svg class="icon plus"><use href="#i-plus"/></svg></div>
    <div class="row"><span class="grow">Skills</span><svg class="icon plus"><use href="#i-plus"/></svg></div>
    <div class="row"><span class="grow">Links</span><svg class="icon plus"><use href="#i-plus"/></svg></div>
    <div class="row"><span class="grow">Awards</span><svg class="icon plus"><use href="#i-plus"/></svg></div>
    <div class="row"><span class="grow">Certifications/Licenses</span><svg class="icon plus"><use href="#i-plus"/></svg></div>
    <div class="row"><span class="grow">Groups</span><svg class="icon plus"><use href="#i-plus"/></svg></div>
    <div class="row"><span class="grow">Patents</span><svg class="icon plus"><use href="#i-plus"/></svg></div>
    <div class="row"><span class="grow">Publications</span><svg class="icon plus"><use href="#i-plus"/></svg></div>
    <nav class="tabbar">
      <div class="tab"><svg class="icon"><use href="#i-home"/></svg>Home</div>
      <div class="tab"><svg class="icon"><use href="#i-search"/></svg>Search</div>
      <div class="tab"><svg class="icon"><use href="#i-jobs"/></svg>My Jobs</div>
      <div class="tab active"><svg class="icon"><use href="#i-cv"/></svg>My CV</div>
      <div class="tab"><svg class="icon"><use href="#i-gear"/></svg>Settings</div>
    </nav>
  </section>

  <!-- Profile -->
  <section class="screen" style="left:793px;top:562px;height:738px">
    <header class="header">
      <div class="status"><span>●●●●● Telvo</span><span>9:41 AM</span><span>100%<span class="bat"></span></span></div>
      <div class="titlebar"><svg class="icon left"><use href="#i-back"/></svg>Profile</div>
    </header>
    <div style="height:30px"></div>
    <div style="border-top:1px solid var(--line)">
      <div class="form-row"><span class="lbl">First name <i>●</i></span>Dane</div>
      <div class="form-row"><span class="lbl">Last name <i>●</i></span>Holloway</div>
      <div class="form-row"><span class="lbl">Email <i>●</i></span>dane@mailbox.com</div>
      <div class="form-row" style="padding-right:0"><span class="lbl">Gender <i>●</i></span><span style="border-left:1px solid var(--line);height:44px;width:96px;display:flex;align-items:center;padding-left:27px;gap:20px">Male<svg class="icon" style="width:16px;height:16px;color:var(--teal)"><use href="#i-chev"/></svg></span></div>
      <div class="form-row"><span class="lbl">Birthday <i>●</i></span>30 Oct 1973</div>
      <div class="form-row"><span class="lbl">City <i>●</i></span>Singapore</div>
      <div class="form-row"><span class="lbl">State</span></div>
      <div class="form-row"><span class="lbl">Country <i>●</i></span>Singapore</div>
    </div>
    <div style="height:30px"></div>
    <div style="position:relative;height:178px;background:var(--row);border-top:1px solid var(--line);border-bottom:1px solid var(--line);font-size:11.5px;color:var(--muted)">
      <div style="position:absolute;left:9px;top:32px">Headline</div>
      <div style="position:absolute;left:72px;top:28px;width:192px;height:21px;border:1px solid var(--divider);background:#fff;font-size:10px;padding:4px 4px;color:#8a9296">Write a headline about me</div>
      <div style="position:absolute;left:9px;top:99px">Headline</div>
      <div style="position:absolute;left:72px;top:56px;width:192px;height:111px;border:1px solid var(--divider);background:#fff"></div>
    </div>
    <div class="btn" style="position:absolute;top:688px;left:47px;width:180px;height:31px">Save</div>
  </section>

  <!-- Settings -->
  <section class="screen" style="left:1149px;top:562px;height:738px">
    <header class="header">
      <div class="status"><span>●●●●● Telvo</span><span>9:41 AM</span><span>100%<span class="bat"></span></span></div>
      <div class="titlebar">Settings</div>
    </header>
    <div style="height:30px;font-size:10px;padding:15px 8px 0;color:#5d676c">NOTIFICAIONS</div>
    <div style="border-top:1px solid var(--line)">
      <div class="row"><span class="grow">Job Messages</span><span class="toggle on"></span></div>
      <div class="row"><span class="grow" style="color:var(--muted)">Send Notifications by Email Too</span><span class="toggle"></span></div>
    </div>
    <div style="height:30px"></div>
    <div style="border-top:1px solid var(--line)">
      <div class="row">Like Us on Chatterly</div>
      <div class="row">Share on Workbrix</div>
      <div class="row">Follow on Chirpline</div>
      <div class="row">Rate Us on AppHub</div>
    </div>
    <div style="height:30px"></div>
    <div style="border-top:1px solid var(--line)">
      <div class="row">Help</div>
      <div class="row">Privacy Policy</div>
      <div class="row">Terms of Use</div>
    </div>
    <div style="height:30px"></div>
    <div style="border-top:1px solid var(--line)">
      <div class="row">Log out</div>
    </div>
    <div style="text-align:center;font-size:11.5px;padding-top:21px">Version 1.2</div>
    <nav class="tabbar">
      <div class="tab"><svg class="icon"><use href="#i-home"/></svg>Home</div>
      <div class="tab"><svg class="icon"><use href="#i-search"/></svg>Search</div>
      <div class="tab"><svg class="icon"><use href="#i-jobs"/></svg>My Jobs</div>
      <div class="tab"><svg class="icon"><use href="#i-cv"/></svg>My CV</div>
      <div class="tab active"><svg class="icon"><use href="#i-gear"/></svg>Settings</div>
    </nav>
  </section>

</div>
</body>
</html>
```